Volora Laundry and Dry Cleaning Poster

We need a Poster and Window Sticker for our Laundry and Dry cleaning shop (VOLORA LAUNDRY AND DRY CLEANING).
info we like on the design. Logo is included
Company Name: Volora Laundry and Dry Cleaning
Slogan: It Comes Back Clean
Location: Kwentu-Dasor, Accra
Working Hours: Mon-Sat 8am to 5pm
Tel: +233 30 781 6242
email:info@voloralaundry.example
website: www.voloralaundry.example
fb: @voloralaundry

Target Market(s)

Laundry Shop

Colors
33a6d7
9bcb3b

```html
<!DOCTYPE html>
<html lang="en">
<head>
<meta charset="utf-8">
<title>Volora Laundry and Dry Cleaning Poster</title>
<link href="https://fonts.googleapis.com/css2?family=Bangers&family=Montserrat:wght@500&family=Oswald:wght@500&display=swap" rel="stylesheet">
<style>
  :root {
    --sky: #33a6d7;
    --lime: #9bcb3b;
    --navy: #0d3a56;
    --sun: #fff200;
    --white: #ffffff;
    --page: #ffffff;
  }
  * { margin: 0; padding: 0; box-sizing: border-box; }
  html, body { width: 1200px; height: 1200px; overflow: hidden; background: var(--page); }
  .poster {
    position: absolute; left: 190px; top: 20px;
    width: 820px; height: 1160px; overflow: hidden;
    background: var(--sky);
  }
  .poster-shapes { position: absolute; inset: 0; }
  .brand {
    position: absolute; left: 464px; top: 30px;
    display: flex; align-items: center; gap: 14px;
  }
  .brand-dot { width: 100px; height: 100px; border-radius: 50%; background: var(--sky); }
  .brand-name {
    font-family: "Montserrat", sans-serif; font-weight: 500;
    font-size: 58px; color: var(--sky); line-height: 1;
  }
  .headline {
    position: absolute; left: 0; width: 100%; text-align: center;
    font-family: "Bangers", cursive; color: var(--sun);
    -webkit-text-stroke: 8px var(--navy); paint-order: stroke fill;
    letter-spacing: 2px; line-height: 1;
  }
  .headline-name { top: 585px; font-size: 158px; }
  .headline-service { top: 744px; font-size: 80px; -webkit-text-stroke-width: 7px; letter-spacing: 1px; }
  .slogan {
    position: absolute; left: 0; width: 100%; top: 858px; text-align: center;
    font-family: "Bangers", cursive; font-size: 86px; color: var(--navy);
    -webkit-text-stroke: 7px var(--white); paint-order: stroke fill;
    transform: rotate(-4deg); line-height: 1; letter-spacing: 1px;
  }
  .contact {
    position: absolute; font-family: "Oswald", sans-serif; font-weight: 500;
    color: var(--white); text-transform: uppercase; line-height: 1;
  }
  .contact-row { position: absolute; display: flex; align-items: center; white-space: nowrap; }
  .contact-icon { width: 22px; height: 22px; margin-right: 8px; flex: none; }
  .contact-label { display: inline-block; }
  .contact-value { position: absolute; }
  .contact-left { left: 22px; top: 1050px; font-size: 21px; letter-spacing: -0.3px; }
  .contact-left .contact-value { left: 192px; }
  .contact-right { left: 474px; top: 1043px; font-size: 18px; letter-spacing: -0.4px; }
  .contact-right .contact-value { left: 112px; font-size: 15.5px; letter-spacing: -0.3px; }
</style>
</head>
<body>
<div class="poster">
  <svg class="poster-shapes" width="820" height="1160" viewBox="0 0 820 1160">
    <defs>
      <linearGradient id="photoTones" x1="0" y1="0" x2="1" y2="0.3">
        <stop offset="0" stop-color="#f07a4a"/>
        <stop offset="0.22" stop-color="#f6c93a"/>
        <stop offset="0.55" stop-color="#f8d93c"/>
        <stop offset="0.78" stop-color="#d9f1e2"/>
        <stop offset="1" stop-color="#9fe0d9"/>
      </linearGradient>
    </defs>
    <polygon role="img" aria-label="Photo of neatly folded stacks of colourful clean T-shirts" points="0,0 820,0 820,580 0,369" fill="url(#photoTones)"/>
    <polygon points="0,369 820,580 820,615 0,374" fill="var(--lime)"/>
    <polygon points="0,374 820,615 0,397" fill="var(--white)"/>
    <polygon points="0,397 820,615 820,1160 0,1160" fill="var(--sky)"/>
    <polygon points="464,1028 820,1028 820,1160 404,1160" fill="var(--navy)"/>
  </svg>

  <div class="brand">
    <span class="brand-dot"></span>
    <span class="brand-name">volora</span>
  </div>

  <h1 class="headline headline-name">VOLORA</h1>
  <p class="headline headline-service">LAUNDRY AND DRY CLEANING</p>
  <p class="slogan">IT COMES BACK CLEAN</p>

  <div class="contact contact-left">
    <div class="contact-row" style="top:0">
      <svg class="contact-icon" viewBox="0 0 22 22"><circle cx="11" cy="11" r="11" fill="#fff"/><path d="M5 11 L11 5.5 L17 11 M7 10 V16 H15 V10" fill="none" stroke="var(--sky)" stroke-width="2"/></svg>
      <span class="contact-label">Location</span><span class="contact-value">: Kwentu-Dasor, Accra</span>
    </div>
    <div class="contact-row" style="top:36px">
      <svg class="contact-icon" viewBox="0 0 22 22"><circle cx="11" cy="11" r="11" fill="#fff"/><path d="M11 17 C7 12 7 10 7 9.5 A4 4 0 0 1 15 9.5 C15 10 15 12 11 17 Z" fill="var(--sky)"/><circle cx="11" cy="9.5" r="1.6" fill="#fff"/></svg>
      <span class="contact-label">Working Hours</span><span class="contact-value">: Mon-Sat 8am to 5pm</span>
    </div>
    <div class="contact-row" style="top:72px">
      <svg class="contact-icon" viewBox="0 0 22 22"><circle cx="11" cy="11" r="11" fill="#fff"/><path d="M7.5 6 L9.5 6 L10.5 8.5 L9 9.5 C9.8 11.3 10.7 12.2 12.5 13 L13.5 11.5 L16 12.5 L16 14.5 C11 15 7 11 7.5 6 Z" fill="var(--sky)"/></svg>
      <span class="contact-label">Tel</span><span class="contact-value">: +233 30 781 6242</span>
    </div>
  </div>

  <div class="contact contact-right">
    <div class="contact-row" style="top:0">
      <svg class="contact-icon" viewBox="0 0 22 22"><circle cx="11" cy="11" r="11" fill="#fff"/><rect x="5.5" y="7" width="11" height="8" fill="var(--navy)"/><path d="M5.5 7 L11 11.5 L16.5 7" fill="none" stroke="#fff" stroke-width="1.3"/></svg>
      <span class="contact-label">Email</span><span class="contact-value">: info@voloralaundry.example</span>
    </div>
    <div class="contact-row" style="top:39px">
      <svg class="contact-icon" viewBox="0 0 22 22"><circle cx="11" cy="11" r="11" fill="#fff"/><g fill="none" stroke="var(--navy)" stroke-width="1.3"><circle cx="11" cy="11" r="6"/><ellipse cx="11" cy="11" rx="2.6" ry="6"/><path d="M5 11 H17"/></g></svg>
      <span class="contact-label">Website</span><span class="contact-value">: www.voloralaundry.example</span>
    </div>
    <div class="contact-row" style="top:78px">
      <svg class="contact-icon" viewBox="0 0 22 22"><circle cx="11" cy="11" r="11" fill="#fff"/><path d="M6 7 H16 V13.5 H10 L7.5 16 V13.5 H6 Z" fill="var(--navy)"/></svg>
      <span class="contact-label">Social</span><span class="contact-value">: @voloralaundry</span>
    </div>
  </div>
</div>
</body>
</html>
```